need a Flyer for Plush Toy company

Need a Flyer for Plush Toy company ,

I upload a file for TEXT

Target Market(s)

Toys wholesalers , Supermarket

Industry/Entity Type

Toy Store

Colors
000000
ec1f27
c4c4c4

Requirements
Must have
• I have up loaded 3 files
• 1. Logo Registered Brand
• 2. customer's design in drawing
• 3. our ready samples based on Design
Nice to have
• happy kids in Nature ,
• happy kids in Ski ,
• different color Kids ,
• Multi culture concept

```html
<!DOCTYPE html>
<html lang="en">
<head>
<meta charset="utf-8">
<title>LUMO TOFU – Plush Toy Flyer</title>
<link href="https://fonts.googleapis.com/css2?family=Kalam:wght@400;700&family=Roboto:wght@400;700&family=Montserrat:wght@700&display=swap" rel="stylesheet">
<style>
  :root {
    --red: #ec1f27;
    --red-dark: #c8141b;
    --black: #000000;
    --grey: #c4c4c4;
    --white: #ffffff;
    --ink: #1a1a1a;
    --stage: #52616a;
  }
  * { box-sizing: border-box; margin: 0; padding: 0; }
  html, body { width: 1200px; height: 1200px; overflow: hidden; background: var(--stage); }
  .flyer {
    position: absolute; left: 187px; top: 20px;
    width: 718px; height: 1008px;
    transform: scale(1.151); transform-origin: 0 0;
    background: linear-gradient(180deg, #f4f4f4 0%, #e9e9e9 55%, #f2f2f2 100%);
    overflow: hidden;
    font-family: "Roboto", Arial, sans-serif;
    color: var(--ink);
  }
  .shapes { position: absolute; inset: 0; }
  .brand-mark { position: absolute; left: 70px; top: 70px; display: flex; align-items: center; gap: 10px; }
  .brand-mark .dot { width: 22px; height: 22px; border-radius: 50%; background: var(--red); }
  .brand-mark .name { font-family: "Montserrat", sans-serif; font-weight: 700; font-size: 26px; color: var(--black); letter-spacing: 1px; }
  .tagline { position: absolute; left: 32px; top: 184px; font-family: "Kalam", cursive; font-size: 24px; color: var(--red); white-space: nowrap; }
  .title { position: absolute; left: 28px; top: 374px; width: 345px; font-family: "Kalam", cursive; font-weight: 700; font-size: 64px; line-height: 1; color: var(--red); letter-spacing: -2px; white-space: nowrap; }
  .subtitle { position: absolute; left: 29px; top: 441px; font-weight: 700; font-size: 16px; color: var(--black); }
  .claims { position: absolute; left: 29px; top: 469px; font-family: "Montserrat", sans-serif; font-weight: 700; font-size: 16.5px; line-height: 23px; color: var(--red); }
  .intro { position: absolute; left: 29px; top: 521px; width: 350px; font-size: 14px; line-height: 18px; text-align: justify; }
  .intro p + p { margin-top: 10px; }
  .intro strong { color: var(--red); font-family: "Montserrat", sans-serif; }
  .info-panel {
    position: absolute; left: 400px; top: 370px; width: 306px; height: 308px;
    background: linear-gradient(160deg, var(--red) 0%, var(--red-dark) 100%);
    border-radius: 0 0 26px 26px; color: var(--white);
    padding: 22px 16px 0 16px; font-size: 13.4px; line-height: 17px;
  }
  .info-panel .offer b { font-weight: 700; font-size: 14.5px; }
  .info-panel .premium { margin-top: 7px; font-weight: 700; }
  .info-panel .line { display: flex; gap: 6px; margin-top: 7px; }
  .info-panel .icon { width: 11px; flex: none; margin-top: 3px; }
  .contacts { margin-top: 8px; font-family: "Montserrat", sans-serif; font-weight: 700; font-size: 13.4px; line-height: 19px; }
  .contacts .mail { display: flex; gap: 6px; align-items: center; }
  .footer { position: absolute; left: 0; top: 902px; width: 718px; height: 106px; background: linear-gradient(180deg, #1c1c1c, var(--black)); border-top: 5px solid var(--red); }
  .footer .label { position: absolute; left: 85px; top: 32px; font-size: 22px; font-weight: 700; color: var(--red); }
  .footer .divider { position: absolute; left: 306px; top: 18px; width: 3px; height: 62px; background: var(--red); }
  .footer .bank { position: absolute; left: 324px; top: 16px; color: var(--white); font-weight: 700; font-size: 13.5px; line-height: 22px; }
</style>
</head>
<body>
<div class="flyer">
  <svg class="shapes" viewBox="0 0 718 1008" width="718" height="1008">
    <defs>
      <linearGradient id="kids-tone" x1="0" y1="0" x2="1" y2="1">
        <stop offset="0" stop-color="#f3d7c4"/><stop offset="0.5" stop-color="#3a7fd1"/><stop offset="1" stop-color="#3bb54a"/>
      </linearGradient>
      <radialGradient id="bear-tone" cx="0.5" cy="0.5" r="0.6">
        <stop offset="0" stop-color="#d7b08b"/><stop offset="1" stop-color="#6b4426"/>
      </radialGradient>
      <linearGradient id="sofa-tone" x1="0" y1="0" x2="0" y2="1">
        <stop offset="0" stop-color="#a9d3a3"/><stop offset="1" stop-color="#86b880"/>
      </linearGradient>
      <linearGradient id="grey-band" x1="0" y1="0" x2="1" y2="0">
        <stop offset="0" stop-color="#b9b9b9"/><stop offset="1" stop-color="#e5e5e5"/>
      </linearGradient>
    </defs>
    <rect x="0" y="0" width="718" height="290" fill="var(--white)"/>
    <path d="M0 268 Q200 262 350 275 L350 320 Q200 300 0 312 Z" fill="var(--red)"/>
    <path d="M0 312 Q200 300 350 320 L350 340 Q200 325 0 355 Z" fill="url(#grey-band)"/>
    <circle cx="600" cy="110" r="270" fill="var(--red)"/>
    <circle cx="612" cy="104" r="257" fill="var(--black)"/>
    <circle cx="622" cy="100" r="250" fill="var(--white)"/>
    <path role="img" aria-label="Photo of happy children in colourful t-shirts cheering with thumbs up" d="M400 30 L690 30 L690 360 L440 360 Q400 200 400 30 Z" fill="url(#kids-tone)" opacity="0.85"/>
    <path d="M420 345 Q560 385 718 320 L718 355 Q560 400 420 370 Z" fill="var(--grey)"/>
    <circle cx="350" cy="270" r="95" fill="var(--red)"/>
    <circle cx="350" cy="270" r="89" fill="var(--white)"/>
    <circle role="img" aria-label="Photo of a girl hugging teddy bears" cx="350" cy="270" r="84" fill="url(#bear-tone)"/>
    <rect role="img" aria-label="Illustration of cartoon plush animals sitting on a green sofa" x="77" y="695" width="565" height="200" rx="14" fill="url(#sofa-tone)"/>
  </svg>

  <div class="brand-mark"><span class="dot"></span><span class="name">LUMO TOFU</span></div>
  <div class="tagline">Have you been there?</div>

  <h1 class="title">LUMO TOFU</h1>
  <div class="subtitle">Einzelunternehmen / Family business</div>
  <div class="claims">Innovative Developer &nbsp;for Plush Toys<br>International Trader for Toys</div>
  <div class="intro">
    <p>We live and work in Lindenfeld near to the Rhine, Germany. We speak German and English.</p>
    <p>The toys are made in China, we are small family business, but we are professional in Plush toys business, right now we have successfully launched Projects with <strong>a huge Japanese 100 Yen Chain Store.</strong></p>
  </div>

  <div class="info-panel">
    <p class="offer"><b>100 Yen = 0.90 USD</b> , Our products can meet strictest Quality Control , but are with extremely Low Price to fit for Japanese Dollar Shop as well as his overseas Store around the world.</p>
    <p class="premium">Of course our products are fit for Premium Store too.</p>
    <div class="line">
      <svg class="icon" viewBox="0 0 10 14" height="14"><path d="M5 0a5 5 0 0 0-5 5c0 4 5 9 5 9s5-5 5-9a5 5 0 0 0-5-5zm0 7a2 2 0 1 1 0-4 2 2 0 0 1 0 4z" fill="var(--white)"/></svg>
      <span>Ahornweg 8, 50999 Lindenfeld<br>Germany</span>
    </div>
    <div class="contacts">
      <div class="mail"><svg viewBox="0 0 10 7" width="10" height="7"><rect width="10" height="7" fill="var(--white)"/><path d="M0 0l5 4 5-4" stroke="var(--red)" fill="none"/></svg>hello@lumotofu-toys.de</div>
      <div>Fon &nbsp;&nbsp;+49 (0) &nbsp;2200- 555 0142</div>
      <div>Fax &nbsp;&nbsp;+49 (0) &nbsp;2200- 555 0143</div>
      <div>Mobil: &nbsp;+49 (0) 170 5550 198</div>
      <div>Ust-IdNr./VAT No. DE000123456</div>
    </div>
  </div>

  <footer class="footer">
    <div class="label">Bank information :</div>
    <div class="divider"></div>
    <div class="bank">
      Kontoinhaber/Account Holder: &nbsp;&nbsp;Mara Feld<br>
      IBAN: &nbsp;DE00 1234 5678 9012 3456 78<br>
      BIC : TESTDEFF000
    </div>
  </footer>
</div>
</body>
</html>
```